Brivo Packworks Website using Wix Platform

Project Overview:
Brivo Packworks is a supply chain company specializing in packaging and manufacturing services for CPG (Consumer Packaged Goods) brands and nutritional/dietary supplement companies. The company offers end-to-end solutions including packaging design, production, co-packing, and private labeling. The goal of this project is to create a professional, user-friendly website that showcases your expertise, builds trust with potential clients, and generates leads for your services.

Objectives:
Establish Brand Authority: Position Brivo Packworks as a leader in the packaging and manufacturing industry for CPG and nutritional products.
Lead Generation: Encourage visitors to contact you for quotes, consultations, or further information.
Professional User Experience: Ensure the website is easy to navigate, visually appealing, and mobile-friendly.
SEO & Conversion Optimization: Optimize the site for search engines to attract organic traffic and improve conversion rates.
Primary Audience:
CPG Brands: Companies in industries like food and beverage, personal care, and household products looking for packaging and manufacturing services.
Nutritional/Dietary Supplement Brands: Companies in the health and wellness industry needing specialized packaging and manufacturing services for supplements, including compliance with regulatory standards (GMP).
Secondary Audience:
Potential partners looking to collaborate on co-packing or private labeling.
Key Features & Functionality:
Responsive Design:

The website must be fully responsive, ensuring optimal viewing across all devices (desktops, tablets, mobile).
User-Centric Navigation:

A clean, intuitive navigation system that allows users to quickly access key pages such as Home, Services, About Us, Case Studies, FAQ, and Contact.
Lead Generation Forms:

Prominent CTAs (Calls to Action) throughout the website encouraging users to “Request a Quote”, “Get in Touch”, or “Learn More” about your services.
Contact Form: Simple form allowing potential clients to submit inquiries about your services.
SEO Optimization:

The site should be optimized for relevant keywords (e.g., “co-packing services for CPG,” “nutritional supplement packaging,” “custom packaging solutions”), including meta descriptions, headers, and on-page content.
Content Management System (CMS):

An easy-to-use CMS (like WordPress or Webflow) for easy content updates. This will allow you to make changes to your services, case studies, and other sections without requiring a developer.
Analytics Integration:

Google Analytics or a similar tool for tracking site visitors and performance metrics to make data-driven decisions on site improvements.
Site Structure & Content:
1. Home Page:
Hero Section with tagline, images or video of your services in action, and a clear CTA (e.g., “Request a Quote”).
Value Proposition: Short and compelling introduction to Brivo Packworks’s core services and advantages.
Overview of Services: Highlight your key offerings (e.g., Packaging Design, Co-packing, Nutritional Supplement Packaging, Private Labeling).
Client Logos/Testimonials: Social proof to establish credibility.
CTA Buttons: Throughout the page to drive conversions (e.g., “Get a Free Consultation”).
2. About Us Page:
Company Overview: Explain your mission, values, and commitment to quality.
Team Overview (Optional): Introduce key team members to humanize your company and build trust.
Core Values and Differentiators: Showcase what makes Brivo Packworks unique—sustainability practices, regulatory compliance, and industry expertise.
3. Services Pages (Separate Pages for Each Service):
Packaging & Design: Custom packaging solutions, materials, and design services for CPG brands.
Manufacturing & Assembly: Your end-to-end production process, assembly capabilities, and how you support both small and large-scale runs.
Nutritional & Dietary Supplement Packaging: Focus on specialized packaging for supplements, regulatory compliance (GMP), and certifications.
Private Labeling: Services for clients who wish to brand their own products using your packaging.
Each service page will include detailed descriptions, benefits, process information, and CTAs like “Get Started” or “Request a Quote”.
4. Case Studies / Portfolio Page:
Success Stories: Showcase in-depth case studies of past projects, especially successful partnerships with CPG or supplement brands.
Before & After Images: Display the difference your services have made for clients, especially in terms of packaging quality or branding improvements.
Client Testimonials: Additional customer feedback to strengthen your brand reputation.
5. FAQ Page:
Address common questions related to lead times, regulatory compliance, order quantities, and specific details for different industries (e.g., dietary supplements).
The format will be accordion-style or dropdowns for easy scanning.
6. Contact Us Page:
Contact Form: With fields for name, email, company, and inquiry details.
Location Information: Physical address, phone number, and working hours.
Map Integration: If relevant, integrate Google Maps to show your office location.
Social Media Links: Link to your company’s LinkedIn, Instagram, or other relevant platforms.

Target Market(s)

Startup CPG Brands, Supplement Brands, Nutrition Brands

Industry/Entity Type

Flexible Packaging, Contract Manufacturing, Supplement & Food Manufacturing

Coding

Coded - Design and coding required

Number of Pages Required

5+ page

Requirements
Must have
• Use our colors.
Nice to have
• https://tornap482.sitebuildhost.example/brivopackworks - www.ninefoldlane.example - www.pelkasnacks.example - thebrightmill.example

```html
<!DOCTYPE html>
<html lang="en">
<head>
<meta charset="utf-8">
<title>Brivo Packworks — Simplifying the Process</title>
<link rel="stylesheet" href="https://fonts.googleapis.com/css2?family=Montserrat:wght@400;500;600;700;800&family=Lato:wght@400;700&family=Roboto:wght@400;500&display=swap">
<style>
:root{
  --navy:#272b41;
  --navy-deep:#1f2336;
  --green:#7fd445;
  --blue:#2f8ee6;
  --band:#2b8de4;
  --ink:#1b1d2a;
  --text:#3b3d4a;
  --muted:#8a8d99;
  --white:#ffffff;
  --field:#ffffff;
}
*{box-sizing:border-box;margin:0;padding:0}
html,body{width:1200px;height:3852px;overflow:hidden}
body{position:relative;background:var(--white);font-family:'Lato',sans-serif;color:var(--text)}
.abs{position:absolute}
a{color:inherit;text-decoration:none}

/* header */
.site-header{position:absolute;left:0;top:0;width:1200px;height:85px;background:var(--navy)}
.brand{position:absolute;display:flex;align-items:center;gap:10px;font-family:'Montserrat',sans-serif;font-weight:500;font-size:26px;color:var(--white);letter-spacing:.5px}
.brand-mark{width:14px;height:14px;background:var(--green)}
.header-brand{left:111px;top:26px}
.nav{position:absolute;top:35px;font-family:'Montserrat',sans-serif;font-size:13px;font-weight:500;color:var(--white)}
.nav.active{color:var(--green)}
.btn{position:absolute;display:flex;align-items:center;justify-content:center;background:var(--green);color:var(--white);font-family:'Montserrat',sans-serif;font-weight:600;font-size:14px;border-radius:3px}

/* hero */
.hero-photo{position:absolute;left:0;top:85px;width:1200px;height:633px;
  background:linear-gradient(90deg,#23252c 0%,#3b3a3a 35%,#7d7468 55%,#a59a8a 72%,#6e6a66 100%)}
.hero-shape{position:absolute;left:0;top:85px}
.hero-title{left:109px;top:186px;font-family:'Montserrat',sans-serif;font-size:54px;line-height:60px;color:var(--white);font-weight:400}
.hero-title b{font-weight:800}
.hero-copy{left:109px;top:321px;width:470px;font-size:15px;line-height:30px;color:var(--white)}

/* about */
.about-frame{left:85px;top:812px;width:428px;height:377px;background:var(--blue)}
.about-photo{left:111px;top:829px;width:428px;height:377px;background:linear-gradient(135deg,#b9c3cc,#7e8f7a 50%,#c9a36d)}
.about-shadow{left:441px;top:1030px;width:162px;height:221px;background:var(--navy)}
.about-product{left:378px;top:1010px;width:216px;height:232px;background:linear-gradient(160deg,#f4f4f4,#d6d6d6)}
.section-h{font-family:'Montserrat',sans-serif;font-size:32px;color:var(--ink);font-weight:400;letter-spacing:.5px}
.section-h b{font-weight:700}
.rule{position:absolute;height:4px;background:var(--blue)}
.about-h{left:643px;top:820px;font-size:30px}
.about-copy{left:643px;top:894px;width:440px;font-size:15px;line-height:28.3px;color:var(--text)}
.about-copy b{color:var(--ink)}
.adv-h{left:643px;top:1047px;font-size:19px;color:var(--blue);font-weight:700}
.adv-list{left:643px;top:1086px;list-style:none;font-size:15px;line-height:28.4px}
.adv-list li{display:flex;align-items:center;gap:12px}
.adv-list li::before{content:"";width:9px;height:9px;border-radius:50%;background:var(--blue)}

/* services */
.services{left:0;top:1373px;width:1200px;height:597px;background:linear-gradient(180deg,#3b4058,#2e3246 60%,#3a3f55)}
.center-h{position:absolute;left:0;width:1200px;text-align:center}
.svc-card{position:absolute;top:1566px;width:222px;height:300px;background:var(--white);text-align:center;padding:0 12px}
.svc-icon{position:absolute;left:81px;top:26px}
.svc-title{position:absolute;left:0;width:100%;font-family:'Montserrat',sans-serif;font-weight:600;font-size:15px;line-height:25px;color:var(--ink)}
.svc-text{position:absolute;left:14px;right:14px;font-size:13.5px;line-height:23px;color:var(--text)}
.svc-link{position:absolute;left:0;width:100%;top:244px;font-family:'Montserrat',sans-serif;font-weight:700;font-size:14px;color:var(--ink);text-decoration:underline}

/* clients */
.client{position:absolute;top:2139px;width:170px;height:129px;background:var(--white);border-radius:8px;box-shadow:0 4px 12px rgba(0,0,0,.12);display:flex;align-items:center;justify-content:center;gap:8px;font-family:'Lato',sans-serif;font-weight:700;font-size:16px;color:var(--navy)}
.client i{width:12px;height:12px;border-radius:50%;background:var(--blue)}
.chev{position:absolute;top:2192px}

/* testimonials */
.testi{left:0;top:2359px;width:1200px;height:561px;background:linear-gradient(135deg,#2f93ea,#2887df)}
.t-card{position:absolute;top:2513px;width:308px;height:326px;border:3px solid var(--white);border-radius:8px;padding:0 24px}
.stars{position:absolute;left:24px;top:26px;color:#f6a623;font-size:14px;letter-spacing:1px}
.t-text{position:absolute;left:24px;right:24px;top:54px;font-family:'Roboto',sans-serif;font-size:14.5px;line-height:25.7px;color:var(--white);text-align:justify}
.t-rule{position:absolute;left:24px;right:24px;top:216px;height:1px;background:rgba(255,255,255,.6)}
.avatar{position:absolute;left:24px;top:240px;width:56px;height:56px;border-radius:50%;background:linear-gradient(135deg,#e9d8c4,#9c8f83)}
.t-name{position:absolute;left:96px;top:242px;font-family:'Roboto',sans-serif;font-weight:500;font-size:19px;color:var(--white)}
.t-place{position:absolute;left:96px;top:270px;font-family:'Roboto',sans-serif;font-size:15px;color:var(--white)}
.t-arrow{position:absolute;top:2675px;width:36px;height:36px;border-radius:50%;background:var(--white);border:2px solid #2481d8;display:flex;align-items:center;justify-content:center}

/* contact */
.field{position:absolute;background:var(--field);box-shadow:0 2px 8px rgba(0,0,0,.12);border-radius:3px;font-size:14px;color:var(--muted);padding:17px 17px}

/* footer */
.footer{left:0;top:3444px;width:1200px;height:408px;background:var(--navy)}
.f-h{position:absolute;top:3512px;font-family:'Montserrat',sans-serif;font-weight:600;font-size:21px;color:var(--white)}
.f-list{position:absolute;top:3550px;list-style:none;font-size:15px;line-height:31px;color:var(--white)}
.f-list li{display:flex;align-items:center;gap:12px}
.f-row{position:absolute;left:838px;display:flex;align-items:center;gap:14px;font-size:15px;color:var(--white)}
.f-icon{width:36px;height:36px;border-radius:50%;background:var(--blue);display:flex;align-items:center;justify-content:center}
.f-line{left:99px;top:3782px;width:1002px;height:1px;background:rgba(255,255,255,.6)}
.copyright{left:0;width:1200px;top:3806px;text-align:center;font-size:15px;color:var(--white)}
</style>
</head>
<body>

<header class="site-header">
  <div class="brand header-brand"><span class="brand-mark"></span>BRIVO PACKWORKS</div>
  <a class="nav active" style="left:506px">HOME</a>
  <a class="nav" style="left:579px">SERVICES</a>
  <a class="nav" style="left:673px">ABOUT US</a>
  <a class="nav" style="left:772px">CASE STUDIES</a>
  <a class="nav" style="left:896px">FAQ</a>
  <a class="btn" style="left:955px;top:19px;width:133px;height:47px;font-size:13px">GET IN TOUCH</a>
</header>

<section>
  <div class="hero-photo" role="img" aria-label="Two warehouse staff checking a packed carton and a tablet between storage shelves"></div>
  <svg class="hero-shape" width="1200" height="633" viewBox="0 0 1200 633" aria-hidden="true">
    <polygon points="0,424 800,598 1200,424 1200,633 0,633" fill="#ffffff"/>
    <polygon points="314,498 800,602 1107,476 800,634" fill="#7fd445"/>
    <polygon points="0,633 1200,633 1200,634 0,634" fill="#ffffff"/>
  </svg>
  <h1 class="abs hero-title">SIMPLIFYING <b>THE<br>PROCESS.</b></h1>
  <p class="abs hero-copy">Brivo Packworks is a family-owned business in Dallas, Texas, with extensive experience in manufacturing and regulatory compliance.</p>
  <a class="btn" style="left:111px;top:396px;width:176px;height:48px">REQUEST A QUOTE</a>
</section>

<section>
  <div class="abs about-frame"></div>
  <div class="abs about-photo" role="img" aria-label="Robotic arm sorting fresh produce crates in a bright warehouse"></div>
  <div class="abs about-shadow"></div>
  <div class="abs about-product" role="img" aria-label="White stand-up protein powder pouch"></div>
  <h2 class="abs section-h about-h"><b>ABOUT BRIVO</b> PACKWORKS</h2>
  <div class="rule" style="left:643px;top:869px;width:71px"></div>
  <p class="abs about-copy">Brivo Packworks is a family-owned business in <b>Dallas, Texas,</b> with extensive experience in manufacturing and regulatory compliance. We simplify the manufacturing process with <b>step-by-step</b> guidance and a friendly customer service team. Let's take brand to the next level!</p>
  <h3 class="abs adv-h">Advantages</h3>
  <ul class="abs adv-list">
    <li>Custom Solutions</li>
    <li>Quality &amp; Compliance</li>
    <li>Fast Turnaround</li>
    <li>Expert Team</li>
  </ul>
  <a class="btn" style="left:643px;top:1218px;width:232px;height:46px;font-size:13px">GET A FREE CONSULTATION</a>
</section>

<section>
  <div class="abs services" role="img" aria-label="Dim production line with bottles on a conveyor under a navy overlay"></div>
  <h2 class="center-h section-h" style="top:1455px;color:#fff">OVERVIEW OF <b>SERVICES</b></h2>
  <div class="rule" style="left:562px;top:1509px;width:75px"></div>

  <div class="svc-card" style="left:111px">
    <svg class="svc-icon" width="60" height="60" viewBox="0 0 60 60"><path d="M8 22 30 12 52 22 30 32Z" fill="#fff" stroke="#272b41" stroke-width="2.5"/><path d="M8 22v22l22 10V32M52 22v22L30 54" fill="#2f8ee6" stroke="#272b41" stroke-width="2.5"/><circle cx="30" cy="14" r="9" fill="#7fd445" stroke="#272b41" stroke-width="2.5"/><path d="M26 14l3 3 5-6" fill="none" stroke="#272b41" stroke-width="2.5"/></svg>
    <div class="svc-title" style="top:106px">PACKAGING DESIGN</div>
    <p class="svc-text" style="top:138px">Lorem ipsum dolor sit amet, consectetur adipiscing elit, sed ut labore et dolore magna aliqua.</p>
    <a class="svc-link">LEARN MORE</a>
  </div>
  <div class="svc-card" style="left:362px">
    <svg class="svc-icon" width="60" height="60" viewBox="0 0 60 60"><circle cx="30" cy="6" r="5" fill="#7fd445" stroke="#272b41" stroke-width="2"/><circle cx="10" cy="20" r="5" fill="#2f8ee6" stroke="#272b41" stroke-width="2"/><circle cx="50" cy="20" r="5" fill="#2f8ee6" stroke="#272b41" stroke-width="2"/><path d="M24 22h12v10l12 20H12l12-20Z" fill="#2f8ee6" stroke="#272b41" stroke-width="2.5"/><circle cx="26" cy="44" r="3" fill="#fff"/><circle cx="34" cy="40" r="2.5" fill="#fff"/></svg>
    <div class="svc-title" style="top:106px">CO-PACKING</div>
    <p class="svc-text" style="top:138px">Lorem ipsum dolor sit amet, consectetur adipiscing elit, sed ut labore et dolore magna aliqua.</p>
    <a class="svc-link">LEARN MORE</a>
  </div>
  <div class="svc-card" style="left:613px">
    <svg class="svc-icon" width="60" height="60" viewBox="0 0 60 60"><ellipse cx="26" cy="10" rx="18" ry="6" fill="#2f8ee6" stroke="#272b41" stroke-width="2.5"/><path d="M8 10v34c0 4 8 6 18 6M44 10v16" fill="none" stroke="#272b41" stroke-width="2.5"/><path d="M8 10v34c0 4 8 6 18 6 4 0 8-1 10-2V26h8V10c0 3-8 6-18 6S8 13 8 10Z" fill="#2f8ee6"/><circle cx="44" cy="42" r="10" fill="#7fd445" stroke="#272b41" stroke-width="2.5"/><circle cx="44" cy="42" r="4" fill="#fff" stroke="#272b41" stroke-width="2"/></svg>
    <div class="svc-title" style="top:96px">NUTRITIONAL<br>SUPPLEMENT PACKAGING</div>
    <p class="svc-text" style="top:154px">Lorem ipsum dolor sit amet, consectetur adipiscing elit, sed ut labore et dolore magna aliqua.</p>
    <a class="svc-link">LEARN MORE</a>
  </div>
  <div class="svc-card" style="left:865px">
    <svg class="svc-icon" width="60" height="60" viewBox="0 0 60 60"><rect x="10" y="18" width="16" height="36" fill="#2f8ee6" stroke="#272b41" stroke-width="2.5"/><rect x="26" y="32" width="24" height="22" fill="#2f8ee6" stroke="#272b41" stroke-width="2.5"/><circle cx="42" cy="14" r="9" fill="#7fd445" stroke="#272b41" stroke-width="2.5"/><circle cx="42" cy="14" r="3.5" fill="#fff"/><rect x="30" y="42" width="16" height="6" fill="#fff" stroke="#272b41" stroke-width="1.5"/></svg>
    <div class="svc-title" style="top:106px">PRIVATE LABELING</div>
    <p class="svc-text" style="top:138px">Lorem ipsum dolor sit amet, consectetur adipiscing elit, sed ut labore et dolore magna aliqua.</p>
    <a class="svc-link">LEARN MORE</a>
  </div>
</section>

<section>
  <h2 class="center-h section-h" style="top:2054px">OUR <b>CLIENTS</b></h2>
  <div class="rule" style="left:564px;top:2103px;width:71px"></div>
  <svg class="chev" style="left:74px" width="18" height="20" viewBox="0 0 18 20"><path d="M12 3 5 10l7 7" fill="none" stroke="#555" stroke-width="2.5"/></svg>
  <div class="client" style="left:117px"><i></i>Rovelle Works</div>
  <div class="client" style="left:313px"><i></i>Marnet City</div>
  <div class="client" style="left:509px"><i></i>Tekvia Systems</div>
  <div class="client" style="left:705px"><i></i>Harlow County</div>
  <div class="client" style="left:901px"><i></i>Pemford Eng.</div>
  <svg class="chev" style="left:1108px" width="18" height="20" viewBox="0 0 18 20"><path d="M6 3l7 7-7 7" fill="none" stroke="#222" stroke-width="2.5"/></svg>
</section>

<section>
  <div class="abs testi"></div>
  <h2 class="center-h section-h" style="top:2414px;color:#fff">CLIENT <b>TESTIMONIALS</b></h2>
  <div class="rule" style="left:558px;top:2472px;width:84px;background:var(--green)"></div>
  <div class="t-arrow" style="left:43px"><svg width="14" height="14" viewBox="0 0 14 14"><path d="M9 2 4 7l5 5" fill="none" stroke="#272b41" stroke-width="2"/></svg></div>
  <div class="t-arrow" style="left:1132px"><svg width="14" height="14" viewBox="0 0 14 14"><path d="M5 2l5 5-5 5" fill="none" stroke="#272b41" stroke-width="2"/></svg></div>

  <div class="t-card" style="left:112px"><div class="stars">★★★★★</div><p class="t-text">Lorem ipsum dolor sit amet, consectetur adipiscing elit, sed do eiusmod tempor incididunt ut labore et dolore magna aliqua ut enim ad minim veniam, quis nostrud exercitation ullamco.</p><div class="t-rule"></div><div class="avatar" role="img" aria-label="Client portrait"></div><div class="t-name">Dana Merrick</div><div class="t-place">Florida, United States</div></div>
  <div class="t-card" style="left:449px"><div class="stars">★★★★★</div><p class="t-text">Lorem ipsum dolor sit amet, consectetur adipiscing elit, sed do eiusmod tempor incididunt ut labore et dolore magna aliqua ut enim ad minim veniam, quis nostrud exercitation ullamco.</p><div class="t-rule"></div><div class="avatar" role="img" aria-label="Client portrait"></div><div class="t-name">Dana Merrick</div><div class="t-place">Florida, United States</div></div>
  <div class="t-card" style="left:784px"><div class="stars">★★★★★</div><p class="t-text">Lorem ipsum dolor sit amet, consectetur adipiscing elit, sed do eiusmod tempor incididunt ut labore et dolore magna aliqua ut enim ad minim veniam, quis nostrud exercitation ullamco.</p><div class="t-rule"></div><div class="avatar" role="img" aria-label="Client portrait"></div><div class="t-name">Dana Merrick</div><div class="t-place">Florida, United States</div></div>
</section>

<section>
  <h2 class="center-h section-h" style="top:2982px"><b>CONTACT</b> US</h2>
  <div class="rule" style="left:556px;top:3035px;width:87px"></div>
  <div class="field" style="left:181px;top:3085px;width:411px;height:49px">Name</div>
  <div class="field" style="left:606px;top:3085px;width:411px;height:49px">Email</div>
  <div class="field" style="left:181px;top:3148px;width:411px;height:49px">Phone Number</div>
  <div class="field" style="left:606px;top:3148px;width:411px;height:49px">Subject</div>
  <div class="field" style="left:181px;top:3210px;width:836px;height:86px">Message</div>
  <a class="btn" style="left:531px;top:3320px;width:136px;height:51px;font-size:15px;box-shadow:0 3px 8px rgba(0,0,0,.15)">Submit</a>
</section>

<footer>
  <div class="abs footer"></div>
  <div class="brand" style="left:112px;top:3548px"><span class="brand-mark"></span>BRIVO PACKWORKS</div>
  <div class="f-h" style="left:428px">Quick Links</div>
  <ul class="f-list" style="left:430px">
    <li>➜ Home</li><li>➜ Services</li><li>➜ About Us</li><li>➜ Case Studies</li><li>➜ FAQ</li><li>➜ Contact</li>
  </ul>
  <div class="f-h" style="left:625px">Other Links</div>
  <ul class="f-list" style="left:627px;top:3548px">
    <li>➜ FAQ</li><li>➜ Terms of Use</li><li>➜ Privacy Policy</li><li>➜ Support Links</li><li>➜ Conditions</li>
  </ul>
  <div class="f-h" style="left:838px">Contact Us</div>
  <div class="f-row" style="top:3562px"><span class="f-icon"><svg width="14" height="18" viewBox="0 0 14 18"><path d="M7 1a6 6 0 0 0-6 6c0 5 6 10 6 10s6-5 6-10a6 6 0 0 0-6-6Z" fill="#fff"/><circle cx="7" cy="7" r="2.3" fill="#2f8ee6"/></svg></span>Brivo Packworks,United State.</div>
  <div class="f-row" style="top:3622px"><span class="f-icon"><svg width="16" height="12" viewBox="0 0 16 12"><rect width="16" height="12" rx="1.5" fill="#fff"/><path d="M1 1l7 6 7-6" fill="none" stroke="#2f8ee6" stroke-width="1.5"/></svg></span>info@brivopackworks.example</div>
  <div class="f-row" style="top:3682px"><span class="f-icon"><svg width="16" height="16" viewBox="0 0 16 16"><path d="M3 1l3 3-2 2c1 2 3 4 5 5l2-2 3 3-2 3C6 15 1 10 0 3Z" fill="#fff"/></svg></span>(555) 214-0392</div>
  <div class="abs f-line"></div>
  <p class="abs copyright">Copyrights@2024.Brivo Packworks.All Rights Reserved</p>
</footer>

</body>
</html>
```